Business card design based on existing website

Please make a business card that is consistent with the look and feel of my new website: http://tellbury.com.sg. By going to the site, I think you'll have all you need in terms of the work I do and the colors I use.

I would like to ask the winner of this project to then do a separate project to design my stationery.

Target Market(s)

Heads of human resources, people wanting psychotherapy, and executives wanting coaching. (It's quite a mix!)

Industry/Entity Type

Psychology

Contact Information for Business Card

Email: ray5678@tellbury.com.sg
Website: http://tellbury.com.sg
Tel: +65 94706218

(I will not have a physical address on the card)

Font styles to use
Serif

Colors

Designer to choose colors to be used in the design.

Requirements
Must have
• On the Front
• ==========
• Have "Dr. Raymond Tellbury" using the font of the website.
• Also "Executive Coach, Psychotherapist, Leadership Professor"
• The back should mention
• ==================
• My degrees
• -------------
• "PhD Kelworth; Post Doc Drayfield". E.g., "Raymond Tellbury (PhD Kelworth; Post Doc Drayfield)" where the text between brackets was in smaller font.
• My work
• ----------
• "Executive coach, psychotherapist, and leadership professor"
• My job titles
• ---------------
• "Principal (Tellbury Consulting)
• Adjunct Professor (Lornvale Commerce University)
• Adjunct Associate Professor (Pemberly Institute of Letters)
• Coach & Supervisor (OKTRAV) '
• Options:
• 1) you can abbreviate Adjunct Professor to "Adj Prof" or "Adj Professor"; and "Adjunct Associate Professor" to "Adj Assoc Prof"
• 2) you abbreviate "Pemberly Institute of Letters" and "Lornvale Commerce University" to "PIL" and "LCU"
• 3) You can also combine the titles for PIL and LCU, e.g., "Adjunct faculty (PIL & LCU)
Nice to have
• Because I work with many Chinese people, it is sometimes helpful to have my family name, "Tellbury", in caps. In the past I have not used caps because it takes away from the aesthetic of the card. Only use caps if it looks good.
• The uploaded image of a "RT" is something that may be helpful. I am undecided.
• THANK YOU for helping me!
Should not have
• No photos. In my industry people consider it overselling.

```html
<!DOCTYPE html>
<html lang="en">
<head>
<meta charset="utf-8">
<title>Dr. Raymond Tellbury – Business Card</title>
<link rel="stylesheet" href="https://fonts.googleapis.com/css2?family=Cormorant+Garamond:ital,wght@0,500;0,600;0,700;1,500&display=swap">
<style>
  :root {
    --forest: #1d4421;
    --forest-deep: #163619;
    --leaf: #4c8a3a;
    --leaf-light: #7fb25f;
    --paper: #f7f7f5;
    --paper-shade: #e4e5e2;
    --ink: #2b2b2b;
    --ink-soft: #555;
    --stage: #ecebe7;
    --serif: "Cormorant Garamond", Georgia, serif;
  }
  * { margin: 0; padding: 0; box-sizing: border-box; }
  html, body { width: 1200px; height: 891px; overflow: hidden; }
  body {
    background: var(--stage);
    font-family: var(--serif);
    display: flex;
    flex-direction: column;
    align-items: center;
    justify-content: center;
    gap: 36px;
  }
  .card {
    position: relative;
    width: 700px;
    height: 400px;
    overflow: hidden;
    box-shadow: 0 6px 18px rgba(0,0,0,0.18);
  }
  .card-art { position: absolute; inset: 0; width: 100%; height: 100%; }

  /* Front */
  .front-name {
    position: absolute;
    top: 142px; left: 0; right: 0;
    text-align: center;
    font-size: 50px;
    font-weight: 600;
    color: var(--ink);
    letter-spacing: 0.5px;
  }
  .front-roles {
    position: absolute;
    top: 208px; left: 0; right: 0;
    text-align: center;
    font-size: 19px;
    font-weight: 500;
    color: var(--ink-soft);
  }
  .front-web {
    position: absolute;
    right: 36px; bottom: 30px;
    font-size: 17px;
    color: var(--paper);
    letter-spacing: 0.5px;
  }
  .dot-row {
    position: absolute;
    left: 340px; bottom: 37px;
    display: flex; gap: 16px;
  }
  .dot-row span {
    width: 5px; height: 5px; border-radius: 50%;
    background: var(--paper);
  }

  /* Back */
  .brand-mark {
    position: absolute;
    left: 26px; top: 138px;
    width: 190px;
    text-align: center;
    color: var(--ink);
  }
  .brand-mark .brand-name {
    font-size: 30px;
    font-weight: 600;
    letter-spacing: 1px;
  }
  .brand-mark .brand-rule {
    width: 120px; height: 1px; margin: 8px auto 0;
    background: var(--ink);
  }
  .back-info {
    position: absolute;
    right: 34px; top: 46px;
    width: 400px;
    color: var(--paper);
    text-align: right;
  }
  .principal {
    font-size: 17px; font-style: italic; font-weight: 500;
    opacity: 0.9;
  }
  .back-name {
    margin-top: 20px;
    font-size: 40px; font-weight: 600; line-height: 1;
  }
  .degrees { font-size: 17px; font-weight: 500; margin-top: 4px; }
  .titles { margin-top: 24px; font-size: 17px; line-height: 1.35; font-weight: 500; }
  .contact-list { margin-top: 18px; list-style: none; }
  .contact-list li {
    display: flex; justify-content: flex-end; align-items: center;
    gap: 10px; font-size: 16px; line-height: 1.9;
  }
  .contact-icon {
    width: 20px; height: 20px;
    border: 1px solid var(--paper);
    display: inline-flex; align-items: center; justify-content: center;
  }
  .contact-icon svg { width: 13px; height: 13px; }
</style>
</head>
<body>

  <section class="card card-front" aria-label="Business card front">
    <svg class="card-art" viewBox="0 0 700 400" preserveAspectRatio="none" aria-hidden="true">
      <rect width="700" height="400" fill="var(--forest)"/>
      <path d="M0 58 Q200 40 420 70 T700 78 V322 Q480 300 300 322 T0 300Z" fill="var(--paper)"/>
      <path d="M0 58 Q200 40 420 70 T700 78 V96 Q560 80 420 90 T0 70Z" fill="var(--paper-shade)"/>
      <path d="M60 66 Q260 52 440 84 T700 92" stroke="var(--leaf)" stroke-width="6" fill="none"/>
      <path d="M0 300 Q150 318 300 306 T700 300" stroke="var(--leaf)" stroke-width="7" fill="none"/>
      <path d="M0 290 Q180 306 320 296 T640 292" stroke="var(--leaf-light)" stroke-width="2" fill="none"/>
    </svg>
    <h1 class="front-name">Dr. Raymond Tellbury</h1>
    <p class="front-roles">Executive Coach · Psychotherapist · Leadership Professor</p>
    <div class="dot-row"><span></span><span></span><span></span><span></span><span></span><span></span><span></span></div>
    <p class="front-web">www.tellbury.com.sg</p>
  </section>

  <section class="card card-back" aria-label="Business card back">
    <svg class="card-art" viewBox="0 0 700 400" preserveAspectRatio="none" aria-hidden="true">
      <rect width="700" height="400" fill="var(--forest-deep)"/>
      <path d="M0 0 H250 L190 400 H0Z" fill="var(--forest)"/>
      <path d="M0 0 H240 L200 262 Q100 250 0 270Z" fill="var(--paper)"/>
      <path d="M0 276 Q100 258 205 270 L196 300 Q100 292 0 310Z" fill="var(--leaf)"/>
      <path d="M0 318 Q100 302 194 310" stroke="var(--leaf-light)" stroke-width="2" fill="none"/>
      <path d="M0 352 Q140 340 320 400" stroke="var(--leaf)" stroke-width="8" fill="none"/>
    </svg>

    <div class="brand-mark">
      <div class="brand-name">Tellbury</div>
      <div class="brand-rule"></div>
    </div>

    <div class="back-info">
      <p class="principal">Principal · Tellbury Consulting</p>
      <h2 class="back-name">Raymond Tellbury</h2>
      <p class="degrees">PhD Kelworth / Post Doc Drayfield</p>
      <p class="titles">Adjunct Faculty · PIL &amp; LCU<br>Coach &amp; Supervisor · OKTRAV</p>
      <ul class="contact-list">
        <li>ray5678@tellbury.com.sg
          <span class="contact-icon"><svg viewBox="0 0 16 16" fill="none" stroke="#f7f7f5" stroke-width="1.4"><rect x="1.5" y="3.5" width="13" height="9"/><path d="M1.5 3.5 L8 9 L14.5 3.5"/></svg></span>
        </li>
        <li>http://tellbury.com.sg
          <span class="contact-icon"><svg viewBox="0 0 16 16" fill="none" stroke="#f7f7f5" stroke-width="1.3"><circle cx="8" cy="8" r="6.3"/><ellipse cx="8" cy="8" rx="2.8" ry="6.3"/><path d="M1.7 8 H14.3"/></svg></span>
        </li>
        <li>+65 94706218
          <span class="contact-icon"><svg viewBox="0 0 16 16" fill="none" stroke="#f7f7f5" stroke-width="1.4"><rect x="4.5" y="1.5" width="7" height="13" rx="1.2"/><path d="M7 12.3 H9"/></svg></span>
        </li>
      </ul>
    </div>
  </section>

</body>
</html>
```